A design led business card for the construction industry

High-end business card to match logo. White logo on dark grey/off black to the front. Matching dark font on white to back, possibly with logo design again.

We offer construction and project management services to commercial and private clients in the UK. Projetcs range from newbuilds, conversion of listed buildings and refurbishments and extensions of existing homes. Our focus is on quality and attention to detail using the highest skills.

Contact Information for Business Card

Name; Dylan Marsh BSc
Position; Project Manager
Mobile; 07961 284 657
Tel; 01632 845192
email; dylan@craftvale.co.uk
web; www.craftvale.co.uk
Address; Fernleigh on Avon, KT4 7PX

Colors

Designer to choose only greyscale colors for use in the design.

Requirements
Must have
• To include the below description of the business,

CONSTRUCTION - PROJECT MANAGEMENT
Nice to have
• The posibility of the top back of the card being used as a ruler. So will have a measurement to scale in mm or an architect scale of 1:50
Should not have
• Should not be portrait

```html
<!DOCTYPE html>
<html lang="en">
<head>
<meta charset="utf-8">
<title>Craft Vale – Business Card</title>
<link rel="stylesheet" href="https://fonts.googleapis.com/css2?family=Montserrat:wght@400;500&family=Roboto:wght@300;400;700&display=swap">
<style>
  :root {
    --bg: #cfd4d3;
    --card-dark: #151515;
    --card-light: #f4f4f3;
    --ink: #1a1a1a;
    --ink-soft: #3a3a3a;
    --ink-light: #f2f2f2;
  }
  * { margin: 0; padding: 0; box-sizing: border-box; }
  html, body {
    width: 1200px;
    height: 1049px;
    overflow: hidden;
    background: var(--bg);
  }
  .stage {
    width: 1200px;
    height: 1049px;
    display: flex;
    flex-direction: column;
    align-items: center;
    justify-content: center;
    gap: 56px;
  }
  .card {
    width: 620px;
    height: 401px;
    position: relative;
    box-shadow: 0 10px 30px rgba(0,0,0,0.18);
  }
  .card--front { background: var(--card-dark); }
  .card--back { background: var(--card-light); color: var(--ink); }

  .brand {
    position: absolute;
    display: flex;
    flex-direction: column;
    align-items: center;
  }
  .brand__square {
    width: 92px;
    height: 92px;
    border: 2px solid currentColor;
  }
  .brand__name {
    margin-top: 18px;
    font-family: "Montserrat", sans-serif;
    font-weight: 400;
    letter-spacing: 0.55em;
    padding-left: 0.55em;
    white-space: nowrap;
  }
  .card--front .brand {
    color: var(--ink-light);
    left: 0; right: 0; top: 110px;
  }
  .card--front .brand__square { width: 120px; height: 120px; }
  .card--front .brand__name { font-size: 22px; margin-top: 24px; }

  .card--back .brand {
    color: var(--ink);
    left: 30px; width: 250px; top: 72px;
  }
  .card--back .brand__name { font-size: 16px; }

  .divider {
    position: absolute;
    left: 296px;
    top: 66px;
    width: 1.5px;
    height: 220px;
    background: var(--ink);
  }
  .contact {
    position: absolute;
    left: 324px;
    top: 72px;
    font-family: "Roboto", sans-serif;
    color: var(--ink-soft);
    font-size: 15px;
    line-height: 1.3;
  }
  .contact__name {
    font-weight: 700;
    color: var(--ink);
    font-size: 15px;
    letter-spacing: 0.01em;
  }
  .contact__role { font-weight: 300; margin-bottom: 12px; }
  .contact__address { font-weight: 300; margin-bottom: 6px; }
  .contact__list { list-style: none; }
  .contact__item {
    display: flex;
    align-items: center;
    gap: 8px;
    font-weight: 300;
    font-size: 15px;
  }
  .contact__item svg { width: 14px; height: 14px; flex: none; }
  .tagline {
    position: absolute;
    left: 0; right: 0;
    bottom: 56px;
    text-align: center;
    font-family: "Roboto", sans-serif;
    font-weight: 300;
    font-size: 15px;
    letter-spacing: 0.02em;
    color: var(--ink-soft);
  }
</style>
</head>
<body>
<main class="stage">
  <section class="card card--front" aria-label="Card front">
    <div class="brand">
      <div class="brand__square"></div>
      <span class="brand__name">CRAFT VALE</span>
    </div>
  </section>

  <section class="card card--back" aria-label="Card back">
    <div class="brand">
      <div class="brand__square"></div>
      <span class="brand__name">CRAFT VALE</span>
    </div>
    <div class="divider"></div>
    <div class="contact">
      <p class="contact__name">DYLAN MARSH BSC</p>
      <p class="contact__role">Project Manager</p>
      <p class="contact__address">Fernleigh on Avon,<br>KT4 7PX</p>
      <ul class="contact__list">
        <li class="contact__item">
          <svg viewBox="0 0 14 14" aria-hidden="true"><rect x="3.5" y="0.8" width="7" height="12.4" rx="1.2" fill="none" stroke="currentColor" stroke-width="1.2"/><line x1="6" y1="11" x2="8" y2="11" stroke="currentColor" stroke-width="1.2"/></svg>
          07961 284 657
        </li>
        <li class="contact__item">
          <svg viewBox="0 0 14 14" aria-hidden="true"><path d="M1 5 Q7 1 13 5 L11.5 6.5 L9.5 5.5 L9.5 4.5 Q7 3.8 4.5 4.5 L4.5 5.5 L2.5 6.5 Z" fill="currentColor"/><path d="M3.5 7 L10.5 7 L12 12.5 L2 12.5 Z" fill="currentColor"/></svg>
          01632 845192
        </li>
        <li class="contact__item">
          <svg viewBox="0 0 14 14" aria-hidden="true"><rect x="1" y="3" width="12" height="8.5" fill="currentColor"/><path d="M1 3 L7 8 L13 3" fill="none" stroke="var(--card-light)" stroke-width="1"/></svg>
          dylan@craftvale.co.uk
        </li>
        <li class="contact__item">
          <svg viewBox="0 0 14 14" aria-hidden="true"><circle cx="7" cy="7" r="5.8" fill="none" stroke="currentColor" stroke-width="1.2"/><ellipse cx="7" cy="7" rx="2.5" ry="5.8" fill="none" stroke="currentColor" stroke-width="1"/><line x1="1.2" y1="7" x2="12.8" y2="7" stroke="currentColor" stroke-width="1"/></svg>
          www.craftvale.co.uk
        </li>
      </ul>
    </div>
    <p class="tagline">CONSTRUCTION - PROJECT MANAGEMENT</p>
  </section>
</main>
</body>
</html>
```